Apartment Complex in Southeastern US needs new signage & identity!

Need a design for a physical sign/logo & signage for a 28 unit apartment complex in West Columbia, South Carolina, USA.

These are properties that, in their market , I would describe as "affordable." They are no-frills accommodations that are safe, clean and inexpensive.

The sign I want foremost is something that will be free-standing (not attached). Approximate measurements of the main finished sign should be about 4' x 6' (but really this is just an aspect ratio of course.)

Ideally also want to have smaller signs of a coordinated design created to denote the building number (maybe even on each door), but that is a secondary task. You'll get an idea for how ugly the current numbering and signage looks in some of the attached photos. Some of the photos also came from the old Chatterly page of the prior management company. (This project could also possibly expand into creating new assets for taking over and rebranding that chatterly page.)

The apartments are currently called "Brenthaw Properties" but frankly speaking I despise this name and want to change (rebrand) it. As the new owner I am thinking to change the name:

Sign should basically say something like the following...

Kesto Apartments
1 & 2 Bedroom Units
3817 Dunmore Creek Rd.
Professionally Managed by
Welkin Properties: (XXX)XXX-XXXX

"Managed by" part should be detachable. For instance if I ever need to change management companies, I'd just want to be able to swap out that part of the sign, not the whole thing, of course.

Another consideration is that it would be good if there could be a "units available" or "move-in-special" part that could be attached to the top based on the property's status.

I think that earth colors are favorable and nice looking for what this is and where it is located.... greens/browns/tans/greys, etc.

Many similar signs I've seen online and in person have an this Civic Dwelling Pledge logo on it (one of the example signs in the attached images appears this way). I may want to have that appear on the sign -- I'm not yet decided.

I'm attaching some logos of similar signs, as well as some photos of the property itself. You can probably also find more information and photos (Orbix Lane Peek.)

I can answer any question or inquiry you might have in pretty short time.

Target Market(s)

- Low-Mid income singles & families in the Southeast US looking for safe & affordable housing

Industry/Entity Type

Apartment

Requirements
Must have
• - A design proposal for an outdoor sign
• - Design for sign should have some 'detachable' parts for the management company, and to indicate whether units are available and
Nice to have
• - "Earthy" colors: tans/browns/greens etc. seem like it might be nice. (The region, [US postal code 29584] has lots and lots of pine trees.)
Should not have
• No comic sans! :)

```html
<!DOCTYPE html>
<html lang="en">
<head>
<meta charset="utf-8">
<title>Kesto Apartments – Sign</title>
<link rel="stylesheet" href="https://fonts.googleapis.com/css2?family=Cinzel:wght@600&family=Kalam:wght@700&family=Arimo:wght@400;700&family=Tinos:wght@400;700&display=swap">
<style>
  :root {
    --teal: #0d6b64;
    --tan: #e8b864;
    --brown: #7a5a2a;
    --stone: #8b8471;
    --forest: #1e6a3a;
    --panel-top: #ffffff;
    --panel-bottom: #c7dfc3;
    --ink: #222;
    --gold-ink: #8a6a10;
    --badge-blue: #1f55a0;
    --frame-blue: #2b4d8e;
  }
  html, body { margin: 0; padding: 0; overflow: hidden; background: #fff; }
  .canvas { width: 1200px; height: 1023px; }
  .sign { display: block; width: 1200px; height: 1023px; }
  .brand-name { font-family: "Arimo", sans-serif; font-weight: 700; fill: var(--forest); }
  .headline { font-family: "Cinzel", serif; font-weight: 600; fill: var(--ink); letter-spacing: 3px; }
  .address { font-family: "Kalam", cursive; font-weight: 700; fill: var(--gold-ink); }
  .managed-label { font-family: "Arimo", sans-serif; fill: var(--ink); }
  .manager { font-family: "Tinos", serif; fill: #333; }
  .zip, .city { font-family: "Arimo", sans-serif; fill: #333; }
  .apartments { font-family: "Tinos", serif; font-weight: 700; fill: #3a3a3a; }
  .available-label { font-family: "Arimo", sans-serif; font-weight: 700; fill: #111; }
</style>
</head>
<body>
<div class="canvas">
<svg class="sign" viewBox="0 0 967 824" preserveAspectRatio="none" xmlns="http://www.w3.org/2000/svg">
  <defs>
    <linearGradient id="panelFill" x1="0" y1="0" x2="0" y2="1">
      <stop offset="0" stop-color="var(--panel-top)"/>
      <stop offset="1" stop-color="var(--panel-bottom)"/>
    </linearGradient>
    <linearGradient id="plateFill" x1="0" y1="0" x2="0" y2="1">
      <stop offset="0" stop-color="#fafafa"/>
      <stop offset="1" stop-color="#b9b7b2"/>
    </linearGradient>
    <linearGradient id="ovalFill" x1="0" y1="0" x2="0" y2="1">
      <stop offset="0" stop-color="#f4f4f4"/>
      <stop offset="1" stop-color="#cfcfcf"/>
    </linearGradient>
  </defs>

  <!-- builder card -->
  <g class="builder-card">
    <rect x="402" y="16" width="156" height="221" fill="#fff" stroke="#666" stroke-width="2"/>
    <rect x="461" y="70" width="38" height="38" fill="var(--forest)"/>
    <text class="brand-name" x="480" y="160" font-size="22" text-anchor="middle">KESTO</text>
    <text class="brand-name" x="480" y="186" font-size="13" text-anchor="middle">CONSTRUCTION</text>
  </g>

  <!-- base blocks -->
  <g class="base">
    <rect x="65" y="578" width="235" height="167" fill="#fff" stroke="var(--teal)" stroke-width="7"/>
    <rect x="82" y="596" width="206" height="132" fill="var(--stone)" stroke="var(--forest)" stroke-width="4"/>
    <rect x="690" y="580" width="215" height="168" fill="#fff" stroke="var(--teal)" stroke-width="7"/>
    <rect x="702" y="598" width="190" height="132" fill="var(--stone)" stroke="var(--forest)" stroke-width="4"/>
  </g>

  <!-- wing beams -->
  <path class="beam" d="M50,352 L192,322 L195,344 L55,376 Z" fill="#fff" stroke="var(--teal)" stroke-width="7"/>
  <path class="beam" d="M917,352 L775,322 L772,344 L912,376 Z" fill="#fff" stroke="var(--teal)" stroke-width="7"/>

  <!-- sign body -->
  <path class="sign-body" d="M96,318 Q483,222 870,318 L870,415 L882,415 L882,700 L96,700 L96,415 Z" fill="#fff" stroke="var(--teal)" stroke-width="8"/>
  <path class="sign-panel" d="M112,332 Q483,262 855,332 L855,690 L112,690 Z" fill="url(#panelFill)" stroke="var(--tan)" stroke-width="5"/>

  <!-- posts -->
  <path d="M162,320 L175,320 L175,440 L190,440" fill="none" stroke="var(--brown)" stroke-width="5"/>
  <path d="M805,320 L792,320 L792,440 L777,440" fill="none" stroke="var(--brown)" stroke-width="5"/>

  <!-- copy -->
  <text class="headline" x="483" y="405" font-size="40" text-anchor="middle">1&amp;2 BEDROOM UNITS</text>
  <text class="address" x="475" y="470" font-size="32" text-anchor="middle">3817 Dunmore Creek Rd.</text>
  <text class="managed-label" x="483" y="534" font-size="32" text-anchor="middle">Professionally Managed by:</text>

  <g class="manager-plate">
    <rect x="173" y="551" width="604" height="53" rx="3" fill="url(#plateFill)" stroke="#999" stroke-width="2"/>
    <text class="manager" x="480" y="590" font-size="30" text-anchor="middle">Welkin Properties: (xxx)xxx-xxxx</text>
  </g>

  <rect class="access-badge" x="125" y="621" width="60" height="58" rx="3" fill="var(--badge-blue)" role="img" aria-label="Accessibility badge"/>

  <g class="availability">
    <text class="available-label" x="783" y="623" font-size="17" text-anchor="middle">Available Ap.</text>
    <rect x="749" y="629" width="68" height="50" rx="5" fill="#fff" stroke="var(--frame-blue)" stroke-width="3"/>
  </g>

  <!-- name oval -->
  <g class="name-oval">
    <ellipse cx="487" cy="703" rx="175" ry="90" fill="#fff" stroke="var(--teal)" stroke-width="8"/>
    <ellipse cx="487" cy="703" rx="160" ry="77" fill="url(#ovalFill)" stroke="var(--teal)" stroke-width="3"/>
    <text class="zip" x="483" y="679" font-size="34" text-anchor="middle">29584</text>
    <text class="city" x="483" y="711" font-size="28" text-anchor="middle">West Columbia SC</text>
    <text class="apartments" x="487" y="756" font-size="38" text-anchor="middle">Apartments</text>
  </g>
</svg>
</div>
</body>
</html>
```